Lumbra K - Premium Business Cards

Background of Lumbra K
Lumbra Kestrelwood is a cigar mobile lounge where guests become family. A place of luxury, relaxation, and ambiance is the global popularity demand. Lumbra Kestrelwood strives to provide first-class service of quality and products. Our goal is to ensure that every guest is treated and serviced as a VIP.

Lumbra Kestrelwood was founded by Desmond Harkavy Jr in January 2020. After 15 years of cigar reviews and research Desmond decided it was time to launch his own cigar brand and boutique cigar company. With a wealth of knowledge and years of experience Lumbra Kestrelwood was born. With opulence for all cultures, Lumbra Kestrelwood offers hand rolled cigars with premium blend tobacco from sweet to bold imported from Costa Rica, Dominican Republic, and Nicaragua. Thank you for your business!

Objective:
Create a business card template to be used for all employees. Design should communicate premium and classy. And should use earth tone colors.

Design should include:
1. Client wants to incorporate the cigar leaf
2. Logo
3. Tagline: Savor every ember
3. Content info:
Calvin Mertzlow
Owner
555-617-0384
cmertzlow@lumbrawares.example
lumbrakestrelwood.example

```html
<!DOCTYPE html>
<html lang="en">
<head>
<meta charset="utf-8">
<title>Lumbra K – Business Cards</title>
<link rel="stylesheet" href="https://fonts.googleapis.com/css2?family=Lato:wght@400;700;900&display=swap">
<style>
  :root {
    --stage: #0d0d0d;
    --card: #2a2a2a;
    --card-edge: #3a3a3a;
    --ink: #ffffff;
    --ink-soft: #d9d9d9;
    --rule: #bdbdbd;
    --emboss-a: #2f2f2f;
    --emboss-b: #3c3c3c;
  }
  * { box-sizing: border-box; margin: 0; padding: 0; }
  html, body { width: 1200px; height: 820px; overflow: hidden; }
  body {
    background: var(--stage);
    font-family: "Lato", Arial, sans-serif;
    color: var(--ink);
    position: relative;
  }
  .card {
    position: absolute;
    top: 260px;
    width: 525px;
    height: 300px;
    background: var(--card);
    border-radius: 3px;
    box-shadow: 0 0 0 1px var(--card-edge);
    overflow: hidden;
  }
  .card--front { left: 50px; }
  .card--back { left: 625px; }

  .wordmark {
    position: absolute;
    text-align: center;
    font-weight: 900;
    text-transform: uppercase;
    color: var(--ink);
    line-height: 1;
  }
  .wordmark__name { display: block; font-size: 46px; letter-spacing: 1px; }
  .wordmark__sub { display: block; font-size: 13px; letter-spacing: 3px; margin-top: 6px; }

  .card--front .wordmark { left: 205px; top: 50px; width: 250px; }
  .card--back .wordmark { left: 0; top: 95px; width: 100%; }

  .rule {
    position: absolute;
    height: 1px;
    background: var(--rule);
  }
  .rule::before, .rule::after {
    content: "";
    position: absolute;
    top: -2px;
    width: 5px; height: 5px;
    border-radius: 50%;
    background: var(--rule);
  }
  .rule::before { left: -2px; }
  .rule::after { right: -2px; }

  .card--front .rule--logo { left: 220px; top: 128px; width: 220px; }
  .card--front .rule--long { left: 30px; top: 162px; width: 465px; }
  .card--front .rule--short { left: 30px; top: 214px; width: 120px; }

  .contact-name {
    position: absolute;
    left: 30px; top: 172px;
    font-size: 17px; font-weight: 700;
    text-transform: uppercase;
    line-height: 20px;
  }
  .contact-role {
    position: absolute;
    left: 30px; top: 192px;
    font-size: 13px; color: var(--ink-soft);
    line-height: 16px;
  }
  .contact-list {
    position: absolute;
    left: 30px; top: 224px;
    list-style: none;
    font-size: 13px;
    line-height: 21px;
  }
  .contact-list li { display: flex; align-items: center; gap: 7px; }
  .contact-list svg { width: 12px; height: 12px; flex: none; }

  .smoke-emboss {
    position: absolute;
    right: 0; top: 0;
    width: 320px; height: 90px;
    background: linear-gradient(160deg, var(--emboss-b), var(--emboss-a) 70%);
    border-bottom-left-radius: 100% 60%;
  }
  .card--back .rule--left { left: 118px; top: 159px; width: 65px; }
  .card--back .rule--right { left: 342px; top: 159px; width: 65px; }
  .tagline {
    position: absolute;
    left: 0; top: 200px; width: 100%;
    text-align: center;
    font-size: 17px; letter-spacing: 2.5px;
    text-transform: uppercase;
    color: var(--ink-soft);
  }
</style>
</head>
<body>
  <section class="card card--front" aria-label="Business card front">
    <div class="wordmark">
      <span class="wordmark__name">Lumbra K</span>
      <span class="wordmark__sub">Kestrelwood</span>
    </div>
    <div class="rule rule--logo"></div>
    <div class="rule rule--long"></div>
    <p class="contact-name">Calvin Mertzlow</p>
    <p class="contact-role">Owner</p>
    <div class="rule rule--short"></div>
    <ul class="contact-list">
      <li>
        <svg viewBox="0 0 12 12" aria-hidden="true"><path d="M2.5 1 L4.5 1 L5.2 3.6 L4 4.6 Q5 7 7.4 8 L8.4 6.8 L11 7.5 L11 9.5 Q10.5 11 9 11 Q1 10 1 3 Q1 1.5 2.5 1 Z" fill="#fff"/></svg>
        555-617-0384
      </li>
      <li>
        <svg viewBox="0 0 12 12" aria-hidden="true"><rect x="0.5" y="2.5" width="11" height="7" fill="#fff"/><path d="M0.5 2.5 L6 7 L11.5 2.5" stroke="#2a2a2a" fill="none"/></svg>
        cmertzlow@lumbrawares.example
      </li>
      <li>
        <svg viewBox="0 0 12 12" aria-hidden="true"><circle cx="6" cy="6" r="5.2" fill="none" stroke="#fff"/><ellipse cx="6" cy="6" rx="2.2" ry="5.2" fill="none" stroke="#fff"/><path d="M1 6 H11" stroke="#fff"/></svg>
        lumbrakestrelwood.example
      </li>
    </ul>
  </section>

  <section class="card card--back" aria-label="Business card back">
    <div class="smoke-emboss" role="img" aria-label="Embossed smoke and cigar leaf decoration"></div>
    <div class="wordmark">
      <span class="wordmark__name">Lumbra K</span>
      <span class="wordmark__sub">Kestrelwood</span>
    </div>
    <div class="rule rule--left"></div>
    <div class="rule rule--right"></div>
    <p class="tagline">Savor every ember</p>
  </section>
</body>
</html>
```